Working Capital graphics

Our business advisory firm requires 9 images to be re-created and improved in the branding of our business.

The 9 images have been uploaded below and the colours and branding of the business can be found at the website www.thornwickadvisory.com.au

```html
<!DOCTYPE html>
<html lang="en">
<head>
<meta charset="UTF-8">
<title>Working Capital</title>
<link rel="stylesheet" href="https://fonts.googleapis.com/css2?family=Arimo&family=Merriweather:wght@700&display=swap">
<style>
  :root {
    --canvas: #ffffff;
    --maroon: #7e141d;
    --orange: #f39325;
    --bubble: #ffffff;
    --title: #ffffff;
  }
  html, body {
    margin: 0;
    padding: 0;
    width: 1200px;
    height: 1000px;
    overflow: hidden;
    background: var(--canvas);
  }
  .diagram {
    display: block;
    width: 1200px;
    height: 1000px;
  }
  .panel { fill: var(--maroon); }
  .hub { fill: var(--orange); }
  .factor { fill: var(--bubble); }
  .factor-label {
    font-family: "Arimo", Arial, sans-serif;
    font-size: 25px;
    fill: var(--maroon);
    text-anchor: middle;
    dominant-baseline: central;
  }
  .hub-title {
    font-family: "Merriweather", Georgia, serif;
    font-weight: 700;
    font-size: 64px;
    fill: var(--title);
    text-anchor: middle;
    dominant-baseline: central;
  }
</style>
</head>
<body>
<svg class="diagram" viewBox="0 0 1200 1000" xmlns="http://www.w3.org/2000/svg" role="img" aria-label="Working Capital and the factors that influence it">
  <rect class="panel" x="122" y="32" width="963" height="935"/>

  <circle class="hub" cx="588" cy="508" r="187"/>
  <text class="hub-title" x="588" y="470">Working</text>
  <text class="hub-title" x="588" y="552">Capital</text>

  <g class="factor-group">
    <circle class="factor" cx="587" cy="143" r="98"/>
    <text class="factor-label" x="587" y="104">Supply</text>
    <text class="factor-label" x="587" y="143">Chain</text>
    <text class="factor-label" x="587" y="182">Issues</text>
  </g>

  <g class="factor-group">
    <circle class="factor" cx="821" cy="228" r="98"/>
    <text class="factor-label" x="821" y="209">Process</text>
    <text class="factor-label" x="821" y="248">Issues</text>
  </g>

  <g class="factor-group">
    <circle class="factor" cx="946" cy="444" r="98"/>
    <text class="factor-label" x="950" y="422">Forecasting</text>
    <text class="factor-label" x="950" y="461">and Planning</text>
  </g>

  <g class="factor-group">
    <circle class="factor" cx="904" cy="688" r="98"/>
    <text class="factor-label" x="906" y="667">Customer</text>
    <text class="factor-label" x="906" y="706">Management</text>
  </g>

  <g class="factor-group">
    <circle class="factor" cx="713" cy="848" r="98"/>
    <text class="factor-label" x="713" y="826">SKU</text>
    <text class="factor-label" x="713" y="865">Complexity</text>
  </g>

  <g class="factor-group">
    <circle class="factor" cx="465" cy="848" r="98"/>
    <text class="factor-label" x="465" y="826">Supplier</text>
    <text class="factor-label" x="465" y="865">Management</text>
  </g>

  <g class="factor-group">
    <circle class="factor" cx="273" cy="690" r="98"/>
    <text class="factor-label" x="273" y="671">KPIs and</text>
    <text class="factor-label" x="273" y="710">Measures</text>
  </g>

  <g class="factor-group">
    <circle class="factor" cx="229" cy="446" r="98"/>
    <text class="factor-label" x="229" y="409">IT Systems</text>
    <text class="factor-label" x="229" y="448">and</text>
    <text class="factor-label" x="229" y="487">Information</text>
  </g>

  <g class="factor-group">
    <circle class="factor" cx="352" cy="228" r="98"/>
    <text class="factor-label" x="352" y="209">Terms and</text>
    <text class="factor-label" x="352" y="248">Conditions</text>
  </g>
</svg>
</body>
</html>
```